UK Supplement Company Needs a Label for Diet Protein Powder

We need a new, modern and fresh design for our Diet Protein Powder. Our protein powder is packaged in black plastic tubs (photo attached) and needs an attractive label. We would like to see designs that grab attention and look professional. We're very open to ideas. The label should be 88mm x 365mm. We also prefer PSD format where possible. These alterations could be made once your design is chosen. Have attached photo of our shake ingredients/benefits.
Updates

Need extra days to review

Target Market(s)

Slimmers

Industry/Entity Type

Health And Wellness

Font styles to use
Serif
Sans Serif

Colors

Designer to choose colors to be used in the design.

Requirements
Must have
• Clean, Modern and Professional Look. Eye catching. The flavour, we offer 6 flavours so this must be something we can edit (Flavours are Banana, Chocolate, Chocolate Mint, Strawberry, Toffee and Vanilla).
Nice to have
• Our logo, this can be BRISK Nutrition or just BRISK. Our logo files are attached.
Should not have
• We do not want to see people (faces or bodies) on the design.

```html
<!DOCTYPE html>
<html lang="en">
<head>
<meta charset="utf-8">
<title>BRISK Nutrition – Low Calorie Protein Shake Label</title>
<link rel="stylesheet" href="https://fonts.googleapis.com/css2?family=Montserrat:wght@300;400;600;700;800&family=Arimo:wght@400;700&display=swap">
<style>
  :root{
    --ink:#1c1d1f;
    --ink-soft:#2b2c2f;
    --lime:#dde32b;
    --lime-deep:#c3cc1c;
    --lime-pale:#eef08a;
    --silver:#d8d8d8;
    --silver-dark:#8a8a8a;
    --white:#ffffff;
    --red:#e52521;
    --panel:rgba(28,29,31,.88);
  }
  *{box-sizing:border-box;margin:0;padding:0}
  html,body{width:1200px;height:290px;overflow:hidden;background:#fff}
  .label{position:relative;width:1200px;height:290px;overflow:hidden;background:var(--ink);font-family:"Montserrat",sans-serif;color:var(--white)}
  .backdrop{position:absolute;inset:0}

  .hero-icon{position:absolute;left:148px;top:32px;width:64px;height:64px;border-radius:50%;
    background:radial-gradient(circle at 40% 35%,#f4f4f4,#9a9a9a);box-shadow:0 0 0 3px #555}

  .brand{position:absolute;left:346px;top:0;width:112px;height:60px;background:#333437;border:1px solid #555;border-top:none;border-radius:0 0 6px 6px;
    display:flex;flex-direction:column;align-items:center;justify-content:center}
  .brand-name{font-weight:700;font-size:22px;letter-spacing:1px;color:#3aa0d8;line-height:1}
  .brand-sub{font-weight:700;font-size:5.5px;letter-spacing:3px;color:#3aa0d8;margin-top:3px}

  .category{position:absolute;left:252px;top:70px;width:312px;display:flex;align-items:center;gap:10px;font-size:11px;letter-spacing:1.5px;font-weight:400;white-space:nowrap}
  .category::before,.category::after{content:"";flex:1;height:2px;background:var(--white)}

  .title{position:absolute;left:0;width:814px;text-align:center;color:var(--lime);line-height:1;letter-spacing:1px;white-space:nowrap}
  .title-top{top:100px;font-weight:300;font-size:36px}
  .title-main{top:140px;font-weight:300;font-size:40px}
  .title-main strong{font-weight:700}

  .stat{position:absolute;top:184px;width:52px;height:52px;border-radius:50%;background:radial-gradient(circle at 50% 35%,#b9bf2a,#858a10);
    box-shadow:0 0 0 3px #d6d6d6,0 0 0 4px #777;display:flex;flex-direction:column;align-items:center;justify-content:center;text-align:center;color:var(--white)}
  .stat b{font-size:15px;font-weight:700;line-height:1}
  .stat span{font-size:7.5px;font-weight:700;line-height:1.2}

  .actives{position:absolute;left:302px;top:252px;display:flex;gap:5px}
  .active{width:38px;font-weight:700;font-size:7.5px;line-height:1.1;text-align:center;color:var(--white);white-space:nowrap}
  .active + .active{border-left:1px solid var(--white);width:43px;padding-left:5px}

  .flavour-art{position:absolute;left:472px;top:192px;width:108px;height:92px;border-radius:40% 50% 45% 40%;
    background:radial-gradient(ellipse at 50% 40%,#f7d55b,#eba82a 60%,#f3efe2 95%)}
  .flavour-name{position:absolute;left:476px;top:258px;font-family:"Arimo",sans-serif;font-size:9.5px;line-height:1.05;color:var(--ink)}

  .origin{position:absolute;left:26px;top:268px;font-family:"Arimo",sans-serif;font-size:6px;color:var(--white)}

  .info{position:absolute;left:824px;top:6px;width:364px;height:274px;background:var(--panel);border-radius:6px}
  .block{position:absolute;left:832px;width:308px;font-family:"Arimo",sans-serif;font-size:7.4px;line-height:1.3;color:var(--white)}
  .block p{padding-left:4px}
  .tag{display:inline-block;width:76px;background:var(--lime);color:var(--ink);font-weight:700;font-size:7.4px;padding:1px 8px;border-radius:0 8px 8px 0;margin-bottom:2px}
  .use{top:14px}
  .ingredients{top:53px}
  .allergens{top:98px}
  .caution{top:212px}

  .facts{position:absolute;left:834px;top:142px;width:308px;height:66px;background:var(--white);border:2px solid #9a9a9a;border-radius:5px;
    display:grid;grid-template-columns:86px 1fr 1fr 1fr 32px;gap:0 4px;padding:3px 4px;color:var(--ink);font-family:"Arimo",sans-serif;font-size:5.4px}
  .facts-head{font-weight:700;font-size:8px;line-height:1.05;border-bottom:2px solid var(--red);padding-bottom:2px}
  .facts-label{display:flex;flex-direction:column;justify-content:space-between;height:100%}
  .facts-label .rows{line-height:1.7}
  .facts-col{border-top:3px solid var(--red)}
  .facts-col div{border-bottom:1px solid var(--red);padding:1px 0;line-height:1.2}
  .facts-col div:first-child{border-bottom-width:2px}
  .facts-size{border-left:2px solid var(--red);padding-left:3px;display:flex;flex-direction:column;justify-content:space-between}
  .facts-size b{font-size:9px;text-align:right}
  .facts-size div{line-height:1.3}

  .maker{position:absolute;left:838px;top:279px;font-family:"Arimo",sans-serif;font-size:5.6px;color:var(--white);white-space:nowrap}
</style>
</head>
<body>
<main class="label">
  <svg class="backdrop" width="1200" height="290" viewBox="0 0 1200 290" aria-hidden="true">
    <defs>
      <linearGradient id="facet" x1="0" y1="0" x2="1" y2="1">
        <stop offset="0" stop-color="#2a2b2e"/><stop offset=".5" stop-color="#1a1b1d"/><stop offset="1" stop-color="#2f3033"/>
      </linearGradient>
      <linearGradient id="chrome" x1="0" y1="0" x2="1" y2="0">
        <stop offset="0" stop-color="#7c7c7c"/><stop offset=".5" stop-color="#f2f2f2"/><stop offset="1" stop-color="#8d8d8d"/>
      </linearGradient>
    </defs>
    <rect width="1200" height="290" fill="url(#facet)"/>
    <path d="M0 0 H60 Q20 20 0 45 Z" fill="var(--lime)"/>
    <path d="M188 0 Q40 140 205 290 L222 290 Q62 140 205 0 Z" fill="url(#chrome)"/>
    <path d="M715 0 Q885 140 795 290 L812 290 Q902 140 733 0 Z" fill="url(#chrome)"/>
    <path d="M230 290 Q500 220 800 290 Z" fill="var(--lime)"/>
    <path d="M780 0 H1200 V290 H795 Q905 140 780 0 Z" fill="var(--lime)"/>
    <path d="M780 0 Q905 140 795 290 H1200 V230 Q1000 200 940 120 Q900 40 1040 0 Z" fill="#2a2b2e"/>
    <path d="M1040 0 Q900 40 940 120 Q1000 200 1200 230 V180 Q1060 150 1010 90 Q990 30 1120 0 Z" fill="var(--lime-pale)" opacity=".7"/>
  </svg>

  <div class="hero-icon" role="img" aria-label="Flexed arm icon in a silver disc"></div>

  <header class="brand">
    <span class="brand-name">BRISK</span>
    <span class="brand-sub">NUTRITION</span>
  </header>

  <p class="category">DIETARY SUPPLEMENT</p>
  <h1 class="title title-top">LOW CALORIE</h1>
  <h2 class="title title-main"><strong>PROTEIN</strong> SHAKE</h2>

  <div class="stat" style="left:250px"><b>4.2</b><span>CARBS</span></div>
  <div class="stat" style="left:313px"><b>117</b><span>CALORIES</span></div>
  <div class="stat" style="left:378px"><b>21G</b><span>PROTEIN</span></div>

  <div class="actives">
    <p class="active">120MG<br>GREEN TEA<br>EXTRACT</p>
    <p class="active">120MG<br>ACAI<br>BERRY</p>
    <p class="active">15MG<br>CLA<br>POWDER</p>
  </div>

  <div class="flavour-art" role="img" aria-label="Bananas splashing into milk"></div>
  <p class="flavour-name">Banana<br>Flavor</p>

  <p class="origin">MADE IN SAMPLE</p>

  <div class="info"></div>

  <section class="block use">
    <span class="tag">SUGGESTED USE:</span>
    <p>Mix one level scoop (30g) with at least 200ml of cold water or skimmed milk in a shaker. Reseal pouch after each use. Store in a cool and dry place.Keep away from children</p>
  </section>

  <section class="block ingredients">
    <span class="tag">INGREDIENTS:</span>
    <p>Protein Blend (<b>Soya</b> Protein Isolate, Whey Protein Concentrate (<b>Milk</b>),<b>Milk Protein</b>)Acetyl-L-Carnitine, Acai Berry Extract, Green Tea extract, CLA Powder, Flavorings, Colourings, Xanthan Gum, Sweetener, Sucralose.</p>
  </section>

  <section class="block allergens">
    <span class="tag">ALLERGENS:</span>
    <p>For allergens, see ingredients in <b>bold</b>. Proceed on equipment which also processes gluten, nuts, egg and peanuts</p>
  </section>

  <section class="facts">
    <div class="facts-label">
      <div class="facts-head">NUTRITION<br>FACTS</div>
      <div class="rows">Sample sample<br>Sample sample<br>Sample sample</div>
    </div>
    <div class="facts-col"><div>Sample sample</div><div>Sample t</div><div>Sample sa</div><div>Sample sample</div><div>Sample sample</div></div>
    <div class="facts-col"><div>Sample sample</div><div>Sample t</div><div>Sample sa</div><div>Sample sample</div><div>Sample sample</div></div>
    <div class="facts-col"><div>Sample sample</div><div>Sample t</div><div>Sample sa</div><div>Sample sample</div><div>Sample sample</div></div>
    <div class="facts-size"><div>Sample t<br>Sample t<br>Sample t<br>Sample t</div><b>1L</b></div>
  </section>

  <section class="block caution">
    <span class="tag">CAUTION:</span>
    <p>This product should not be used as a subtitute for a balanced and healthy lifestyle. Not recommended for use by pregnant or lactating women. If you are taking any medications or under medical supervision, you should consult with your GP before use. Not intended for use by persons under the age of 18. Not intended for long term usage.</p>
  </section>

  <p class="maker">Manufactured in the UK for Brisk Nutrition Limited, Mill Lane, Northbridge, NB4 2QT. Expiry: See back pouch.</p>
</main>
</body>
</html>
```